KT Crewing business card

Require business card which includes:
Company name: KT CREWING PTY LTD
Email: Mick@ktcrewing.com.au
Phone: 0431 556 208
ACN: 517 238 649

slogan: Onsite Auto Electrician Labour hire

Details and logo on top side
Logo only on bottom side

colour codes : #F15A29 , #939598

Target Market(s)

Western Australia mining sector

Industry/Entity Type

Mining

Contact Information for Business Card

Require business card which includes: Company name: KT CREWING PTY LTD Email: Mick@ktcrewing.com.au Phone: 0431 556 208 ACN: 517 238 649 slogan: Onsite Auto Electrician Labour hire Details and logo on top side Logo only on bottom side colour codes : #F15A29 , #939598

Colors
EE7325
F08F49
F5BC92
FAE3D3
FDF4ED

Requirements
Must have
• double sided

```html
<!DOCTYPE html>
<html lang="en">
<head>
<meta charset="utf-8">
<title>KT Crewing Business Card</title>
<link rel="stylesheet" href="https://fonts.googleapis.com/css2?family=Open+Sans:wght@400;700;800&display=swap">
<style>
  :root {
    --orange: #F15A29;
    --grey: #939598;
    --ink: #4a4a4c;
    --card: #ffffff;
    --backdrop: #2e2f31;
  }
  * { margin: 0; padding: 0; box-sizing: border-box; }
  html, body {
    width: 1200px; height: 900px; overflow: hidden;
    background: var(--backdrop);
    font-family: "Open Sans", Arial, sans-serif;
  }
  .stage {
    width: 1200px; height: 900px;
    display: flex; flex-direction: column; align-items: center; justify-content: center;
    gap: 40px;
  }
  .card {
    position: relative;
    width: 700px; height: 400px;
    background: var(--card);
    overflow: hidden;
  }

  /* Logo side */
  .card-logo {
    display: flex; flex-direction: column; align-items: center; justify-content: center;
  }
  .brand-mark {
    display: flex; align-items: center; gap: 16px;
  }
  .brand-square {
    width: 30px; height: 30px; background: var(--orange);
  }
  .brand-name {
    font-weight: 800; font-size: 64px; line-height: 1; color: var(--orange);
    letter-spacing: -0.5px;
  }
  .rule {
    width: 470px; height: 2px; background: var(--orange); margin: 26px 0 14px;
  }
  .slogan {
    font-weight: 700; font-size: 19px; color: var(--grey); letter-spacing: 1.5px;
  }

  /* Details side */
  .card-details .identity {
    position: absolute; left: 70px; top: 90px; width: 300px;
  }
  .card-details .brand-name { font-size: 54px; }
  .card-details .brand-square { width: 26px; height: 26px; }
  .legal-name {
    margin-top: 14px;
    font-size: 21px; font-weight: 400; color: var(--grey); letter-spacing: 0.5px;
  }
  .divider {
    position: absolute; left: 388px; top: 60px; width: 2px; height: 170px; background: var(--grey);
  }
  .contact {
    position: absolute; left: 420px; top: 76px;
    list-style: none; font-size: 19px; color: var(--ink); line-height: 1.7;
  }
  .contact .label { color: var(--orange); font-weight: 700; margin-right: 6px; }
  .band {
    position: absolute; left: 0; right: 0; bottom: 38px; height: 80px;
    background: var(--orange);
    display: flex; align-items: center; justify-content: center;
  }
  .band .slogan { color: #fff; font-size: 22px; }
</style>
</head>
<body>
<main class="stage">
  <section class="card card-logo" aria-label="Card back">
    <div class="brand-mark">
      <span class="brand-square"></span>
      <span class="brand-name">KT Crewing</span>
    </div>
    <div class="rule"></div>
    <p class="slogan">Onsite Auto Electrician Labour hire</p>
  </section>

  <section class="card card-details" aria-label="Card front">
    <div class="identity">
      <div class="brand-mark">
        <span class="brand-square"></span>
        <span class="brand-name">KT Crewing</span>
      </div>
      <p class="legal-name">KT CREWING PTY LTD</p>
    </div>
    <div class="divider"></div>
    <ul class="contact">
      <li><span class="label">P.</span>0431 556 208</li>
      <li><span class="label">E.</span>Mick@ktcrewing.com.au</li>
      <li><span class="label">ACN:</span>517 238 649</li>
    </ul>
    <div class="band"><p class="slogan">Onsite Auto Electrician Labour hire</p></div>
  </section>
</main>
</body>
</html>
```